METAL FABRICATION BUSINESS CARD

** I will be ending the project and picking design early. This Friday October 3rd at 7am MST if not sooner**
ONE SIDED BUSINESS CARD ONLY. AND LOGO SIZE TO BE DOMINANT so it stands out.
Looking for a black background and will be doing raised chrome/silver font on the business cards. Looking to have the following on the front of the business card. Company logo is uploaded in files.
Company logo
*Compartment Doors
*Roof Radius Metal
*J-Wrap Metal Skirting
*S-Lock Beltline Molding
*Pre-Bent Molding
and more...
Owen Daltry 307.552.4198 info@KX-Welt.com
Updates
One sided business card only please. Also logo size should be dominant and sized bigger
Contact Information for Business Card
Black background, Text will be raised chrome/silver, and corners will be rounded.

```html
<!DOCTYPE html>
<html lang="en">
<head>
<meta charset="utf-8">
<title>KX-Welt Business Card</title>
<link href="https://fonts.googleapis.com/css2?family=Lato:wght@400;900&display=swap" rel="stylesheet">
<style>
  :root {
    --backdrop: #1c1c1e;
    --card-black: #0b0b0c;
    --chrome-light: #eef0f2;
    --chrome-mid: #b9bdc2;
    --chrome-dark: #6d7177;
    --text-silver: #d9dcdf;
  }
  html, body {
    margin: 0;
    width: 1200px;
    height: 923px;
    overflow: hidden;
    background: var(--backdrop);
  }
  .card {
    position: absolute;
    left: 120px;
    top: 181px;
    width: 960px;
    height: 560px;
    border-radius: 34px;
    overflow: hidden;
    background: linear-gradient(115deg, var(--chrome-dark) 0%, var(--chrome-light) 35%, var(--chrome-mid) 60%, var(--chrome-light) 85%, var(--chrome-dark) 100%);
    font-family: "Lato", sans-serif;
    color: var(--text-silver);
  }
  .card-face {
    position: absolute;
    inset: 0;
  }
  .brand {
    position: absolute;
    left: 150px;
    top: 90px;
    display: flex;
    align-items: center;
    gap: 26px;
  }
  .brand-dot {
    width: 96px;
    height: 96px;
    border-radius: 50%;
    background: var(--text-silver);
  }
  .brand-name {
    font-weight: 900;
    font-size: 150px;
    line-height: 1;
    letter-spacing: -2px;
    color: var(--text-silver);
  }
  .services {
    position: absolute;
    left: 560px;
    top: 270px;
    margin: 0;
    padding: 0;
    list-style: none;
    font-size: 21px;
    line-height: 31px;
  }
  .services li {
    display: flex;
    align-items: center;
    gap: 10px;
  }
  .services .tick {
    width: 16px;
    height: 16px;
    flex: none;
  }
  .services .more {
    padding-left: 26px;
  }
  .contact {
    position: absolute;
    left: 170px;
    top: 380px;
  }
  .contact-name {
    font-weight: 900;
    font-size: 30px;
    letter-spacing: 2px;
    text-transform: uppercase;
    margin: 0 0 8px;
  }
  .contact-line {
    display: flex;
    align-items: center;
    gap: 12px;
    font-size: 23px;
    line-height: 34px;
  }
  .contact-line svg {
    width: 16px;
    height: 16px;
  }
</style>
</head>
<body>
  <div class="card">
    <svg class="card-face" viewBox="0 0 960 560" width="960" height="560" aria-hidden="true">
      <path d="M250,0 L830,0 C905,70 930,190 930,280 C930,380 905,480 845,560 L175,560 C85,470 65,300 120,165 C150,95 200,35 250,0 Z" fill="var(--card-black)"/>
    </svg>

    <div class="brand">
      <span class="brand-dot"></span>
      <span class="brand-name">KX-Welt</span>
    </div>

    <ul class="services">
      <li><svg class="tick" viewBox="0 0 16 16"><circle cx="8" cy="8" r="8" fill="var(--chrome-mid)"/><path d="M4.5 8.2 L7 10.6 L11.5 5.6" stroke="var(--card-black)" stroke-width="2" fill="none"/></svg>Compartment Doors</li>
      <li><svg class="tick" viewBox="0 0 16 16"><circle cx="8" cy="8" r="8" fill="var(--chrome-mid)"/><path d="M4.5 8.2 L7 10.6 L11.5 5.6" stroke="var(--card-black)" stroke-width="2" fill="none"/></svg>Roof Radius Metal</li>
      <li><svg class="tick" viewBox="0 0 16 16"><circle cx="8" cy="8" r="8" fill="var(--chrome-mid)"/><path d="M4.5 8.2 L7 10.6 L11.5 5.6" stroke="var(--card-black)" stroke-width="2" fill="none"/></svg>J-Wrap Metal Skirting</li>
      <li><svg class="tick" viewBox="0 0 16 16"><circle cx="8" cy="8" r="8" fill="var(--chrome-mid)"/><path d="M4.5 8.2 L7 10.6 L11.5 5.6" stroke="var(--card-black)" stroke-width="2" fill="none"/></svg>S-Lock Beltline Molding</li>
      <li><svg class="tick" viewBox="0 0 16 16"><circle cx="8" cy="8" r="8" fill="var(--chrome-mid)"/><path d="M4.5 8.2 L7 10.6 L11.5 5.6" stroke="var(--card-black)" stroke-width="2" fill="none"/></svg>Pre-Bent Molding</li>
      <li class="more">and more...</li>
    </ul>

    <div class="contact">
      <p class="contact-name">Owen Daltry</p>
      <div class="contact-line">
        <svg viewBox="0 0 16 16"><path d="M3 1 L6 1 L7 5 L5 6.5 C6 9 7 10 9.5 11 L11 9 L15 10 L15 13 C15 14 14 15 13 15 C6 15 1 10 1 3 C1 2 2 1 3 1 Z" fill="var(--text-silver)"/></svg>
        <span>307.552.4198</span>
      </div>
      <div class="contact-line">
        <svg viewBox="0 0 16 16"><rect x="1" y="3" width="14" height="10" fill="var(--text-silver)"/><path d="M1 3 L8 9 L15 3" stroke="var(--card-black)" stroke-width="1.5" fill="none"/></svg>
        <span>info@KX-Welt.com</span>
      </div>
    </div>
  </div>
</body>
</html>
```